Larkfield Compliance Partners - Invitation for a get together

We are in need of an invitation for an upcoming gathering we are having with our clients. The gathering will be in Tobin's Bar in Manly. http://www.tobinsbar.example/. Tobins bar is described as a New York loft style bar.

We are a building and construction consulting firm, our clients include firms such as Grevo Pike, Osprey Vale, Caldrik.

We are seeking to thank our clients for their support with a Friday afternoon drinks at Tobins Bar. We will be providing food and drinks.

Details are:-

When - Friday 19 September 2014
Time - 4pm onwards
Where - 12 Quarry Row Manly

I would like a map to appear on the invite indicating where the bar is. I would also like

Target Market(s)

Clients, such as property developers, architects, builders

Industry/Entity Type

Construction

Colors

Designer to choose colors to be used in the design.

Requirements
Must have
• Details of what the invite is for, i.e. Larkfield Compliance Partners invites you to Tobins Bar at Manly for a casual drink and get together.

Details of the event i.e. Date, time, Location
Nice to have
• We hope the invite will have a sophisticated feel about it, like a trendy New York bar

```html
<!DOCTYPE html>
<html lang="en">
<head>
<meta charset="utf-8">
<title>Larkfield Compliance Partners – Invitation</title>
<link rel="stylesheet" href="https://fonts.googleapis.com/css2?family=Cinzel:wght@700&family=Didact+Gothic&family=Josefin+Sans:wght@400&family=Lobster&display=swap">
<style>
  :root {
    --slate: #5e6f7c;
    --band-blue: #4f66b0;
    --ink-blue: #2b3190;
    --ink-dark: #1f1f1f;
    --ink-grey: #3d3d3d;
    --paper: #ffffff;
  }
  * { margin: 0; padding: 0; box-sizing: border-box; }
  html, body { width: 848px; height: 1200px; overflow: hidden; background: var(--paper); }
  .invitation { position: relative; width: 848px; height: 1200px; background: var(--paper); font-family: "Didact Gothic", sans-serif; }

  .edge { position: absolute; left: 0; width: 100%; }
  .edge--top { top: 0; height: 108px; background: var(--slate); }
  .edge--bottom { bottom: 0; height: 107px; background: var(--slate); }
  .stitch-band { position: absolute; left: 0; width: 100%; height: 27px; background: var(--band-blue); }
  .stitch-band::after { content: ""; position: absolute; left: 0; right: 0; top: 12px; border-top: 2px dashed var(--paper); }
  .stitch-band--top { top: 108px; }
  .stitch-band--bottom { top: 1066px; }

  .ornament { position: absolute; left: 374px; width: 100px; height: 34px; border-radius: 17px; background: var(--slate); opacity: 0.85; }
  .ornament--upper { top: 215px; }
  .ornament--lower { top: 864px; }

  .host { position: absolute; top: 305px; left: 0; width: 100%; text-align: center; font-family: "Josefin Sans", sans-serif; font-weight: 400; font-size: 42px; letter-spacing: 1px; color: var(--ink-blue); }
  .lead-in { position: absolute; top: 378px; left: 0; width: 100%; display: flex; justify-content: center; align-items: center; gap: 14px; font-family: "Didact Gothic", sans-serif; font-size: 21px; letter-spacing: 2px; color: var(--ink-grey); }
  .lead-in::before, .lead-in::after { content: ""; width: 92px; border-top: 1.5px solid var(--ink-grey); }

  .venue { position: absolute; top: 432px; left: 0; width: 100%; text-align: center; font-family: "Cinzel", serif; font-weight: 700; font-size: 40px; color: var(--ink-dark); }
  .occasion { position: absolute; top: 480px; left: 0; width: 100%; text-align: center; font-family: "Cinzel", serif; font-weight: 700; font-size: 23px; color: var(--ink-dark); }

  .detail { position: absolute; left: 0; width: 848px; height: 53px; }
  .detail--date { top: 562px; }
  .detail--time { top: 660px; }
  .detail--location { top: 754px; }
  .detail__ribbon { position: absolute; left: 0; top: 0; }
  .detail__label { position: absolute; left: 0; top: 0; width: 240px; line-height: 53px; text-align: center; font-family: "Lobster", cursive; font-size: 34px; color: var(--paper); }
  .detail__value { position: absolute; left: 296px; top: 0; line-height: 53px; font-family: "Didact Gothic", sans-serif; font-size: 32px; color: var(--ink-dark); }

  .signature { position: absolute; top: 950px; left: 0; width: 100%; display: flex; justify-content: center; align-items: center; gap: 16px; }
  .signature__mark { width: 44px; height: 44px; background: var(--ink-blue); }
  .signature__name { font-family: "Josefin Sans", sans-serif; font-weight: 400; font-size: 22px; line-height: 1.15; letter-spacing: 1px; color: var(--ink-blue); }
</style>
</head>
<body>
<main class="invitation">
  <div class="edge edge--top"></div>
  <div class="stitch-band stitch-band--top"></div>

  <div class="ornament ornament--upper" role="img" aria-label="Decorative flourish with dots"></div>

  <h1 class="host">LARKFIELD COMPLIANCE PARTNERS</h1>
  <p class="lead-in">INVITES YOU TO</p>
  <h2 class="venue">Tobins Bar at Manly</h2>
  <p class="occasion">FOR A CASUAL DRINK AND GET TOGETHER</p>

  <div class="detail detail--date">
    <svg class="detail__ribbon" width="274" height="53" viewBox="0 0 274 53" aria-hidden="true"><polygon points="0,0 274,0 238,26.5 274,53 0,53" fill="#4f66b0"/></svg>
    <span class="detail__label">Date</span>
    <span class="detail__value">Friday 19 September 2014</span>
  </div>
  <div class="detail detail--time">
    <svg class="detail__ribbon" width="274" height="53" viewBox="0 0 274 53" aria-hidden="true"><polygon points="0,0 274,0 238,26.5 274,53 0,53" fill="#4f66b0"/></svg>
    <span class="detail__label">Time</span>
    <span class="detail__value">4pm onwards</span>
  </div>
  <div class="detail detail--location">
    <svg class="detail__ribbon" width="274" height="53" viewBox="0 0 274 53" aria-hidden="true"><polygon points="0,0 274,0 238,26.5 274,53 0,53" fill="#4f66b0"/></svg>
    <span class="detail__label">Location</span>
    <span class="detail__value">12 Quarry Row, Manly</span>
  </div>

  <div class="ornament ornament--lower" role="img" aria-label="Decorative flourish with dots"></div>

  <div class="signature">
    <span class="signature__mark" aria-hidden="true"></span>
    <span class="signature__name">LARKFIELD<br>COMPLIANCE PARTNERS</span>
  </div>

  <div class="stitch-band stitch-band--bottom"></div>
  <div class="edge edge--bottom"></div>
</main>
</body>
</html>
```